Fun footwear company needs a media card!

We are a fun footwear company called 'Puddle Pops' we are looking for a small media card to be sent out with our products.
The media card will showcase or newest product 'Puddle Ponchos' - it needs to include a small caption reading
'Hello, adventurer. It’s time to stomp around in the rain.Tag your travels @gosplashwild #ppops or visit us at facebook.com/gosplashwild'
We would like to include or logo (attached)
Also have something similar to the previous media card (attached)
I have attached an image of the product (please feel free to not include this is you think it does not work)
As we are a fun brand, all of our promotional media needs to be bright and fit in with our brand.
Visit our website to see our products www.pudpops.com.au

```html
<!DOCTYPE html>
<html lang="en">
<head>
<meta charset="utf-8">
<title>Puddle Pops – Media Card</title>
<link rel="stylesheet" href="https://fonts.googleapis.com/css2?family=Bubblegum+Sans&family=PT+Sans:ital,wght@0,400;0,700;1,700&display=swap">
<style>
  :root {
    --pop-red: #e4242c;
    --pop-blue: #33a4d9;
    --paper: #ffffff;
    --mark: #9a9a9a;
    --frame: 5px;
  }
  html, body {
    margin: 0;
    padding: 0;
    overflow: hidden;
    background: var(--paper);
  }
  .sheet {
    position: relative;
    width: 1187px;
    height: 1200px;
    background: var(--paper);
    overflow: hidden;
  }
  .crop-mark {
    position: absolute;
    width: 1px;
    height: 36px;
    background: var(--mark);
  }
  .crop-mark.top { top: 0; }
  .crop-mark.bottom { bottom: 0; }

  .panel {
    position: absolute;
    top: 57px;
    width: 488px;
    height: 1085px;
  }
  .panel--front { left: 59px; }
  .panel--back { left: 641px; }

  .frame-half {
    position: absolute;
    left: 0;
    width: 100%;
    box-sizing: border-box;
    pointer-events: none;
  }
  .frame-half--top {
    top: 0;
    height: 543px;
    border: var(--frame) solid var(--pop-red);
    border-bottom: none;
  }
  .frame-half--bottom {
    top: 543px;
    height: 542px;
    border: var(--frame) solid var(--pop-blue);
    border-top: none;
  }

  .brand-name {
    position: absolute;
    left: 50%;
    top: 50%;
    transform: translate(-50%, -50%) rotate(90deg);
    white-space: nowrap;
    font-family: "Bubblegum Sans", sans-serif;
    font-size: 150px;
    line-height: 1;
    color: var(--pop-red);
    margin: 0;
  }

  .headline {
    position: absolute;
    top: 28px;
    left: 0;
    width: 100%;
    margin: 0;
    text-align: center;
    font-family: "Bubblegum Sans", sans-serif;
    font-weight: 400;
    font-size: 62px;
    line-height: 54px;
    letter-spacing: 1px;
    color: var(--pop-red);
    text-transform: uppercase;
  }

  .product-photo {
    position: absolute;
    left: var(--frame);
    right: var(--frame);
    top: 168px;
    height: 594px;
    background: linear-gradient(180deg, #ffffff 0%, #eef3f7 45%, #dbe6ee 100%);
  }

  .tagline-band {
    position: absolute;
    left: var(--frame);
    right: var(--frame);
    top: 762px;
    height: 213px;
    background: var(--pop-blue);
    display: flex;
    align-items: center;
    justify-content: center;
  }
  .tagline {
    margin: 0;
    text-align: center;
    font-family: "PT Sans", sans-serif;
    font-weight: 700;
    font-style: italic;
    font-size: 49px;
    line-height: 61px;
    color: var(--paper);
  }

  .social {
    position: absolute;
    left: 0;
    width: 100%;
    top: 992px;
    margin: 0;
    text-align: center;
    font-family: "PT Sans", sans-serif;
    font-size: 23px;
    line-height: 33px;
    color: var(--pop-blue);
  }
  .social strong { font-weight: 700; }
</style>
</head>
<body>
<div class="sheet">
  <span class="crop-mark top" style="left:42px"></span>
  <span class="crop-mark top" style="left:567px"></span>
  <span class="crop-mark top" style="left:620px"></span>
  <span class="crop-mark top" style="left:1149px"></span>
  <span class="crop-mark bottom" style="left:42px"></span>
  <span class="crop-mark bottom" style="left:567px"></span>
  <span class="crop-mark bottom" style="left:620px"></span>
  <span class="crop-mark bottom" style="left:1149px"></span>

  <section class="panel panel--front">
    <div class="frame-half frame-half--top"></div>
    <div class="frame-half frame-half--bottom"></div>
    <p class="brand-name">Puddle Pops</p>
  </section>

  <section class="panel panel--back">
    <h1 class="headline">Hello,<br>Adventurer</h1>
    <div class="product-photo" role="img" aria-label="Model wearing a clear Puddle Ponchos raincoat with blue trim over a white top and striped skirt"></div>
    <div class="tagline-band">
      <p class="tagline">It’s time to<br>stomp around<br>in the rain</p>
    </div>
    <p class="social">Tag your travels <strong>@gosplashwild #ppops</strong><br>or visit us at <strong>facebook.com/gosplashwild</strong></p>
    <div class="frame-half frame-half--top"></div>
    <div class="frame-half frame-half--bottom"></div>
  </section>
</div>
</body>
</html>
```